New, modern business card for growing audiology practice

We need a new business card for our audiology practice. Our logo and website have recently changed (more modern) and we want our business cards to reflect this change.
We conduct hearing tests, perform earwax removals, and fit & dispense hearing aids to our patients. We are a family owned practice in which the owner is the one who works directly with the patient. I have attached logos in various formats to use, as well as two ideas I found on this website; as well as a scanned copy of our current logo. Good luck!

Industry/Entity Type

Business

Contact Information for Business Card

Company name: Maplow Hearing Center
Provider name: Peter Mulvoy, Au.D. F/ISN
Phone number: (555) 318-6042
Address: 87 W. Linden Ave. Brookvale, OH 44961
email: maplowhearing@postvale.net
website: maplowhearing.com

Colors
000000
aaaaaa
dbdbdb
cacaca
9bcb3c
afd23c
cadf82
b1b1b1

Requirements
Must have
• My card must include information in the "details" section. In the attached images, I found a few that I liked and I would like to model after - "brisk tumblin'" and "Sound Wellness Center".
• Must be horizontal.
• Must include logos provided. I uploaded them in various file formats and various ways.
• Must match logo font, if possible, if not, please get as close as you can.
Nice to have
• I really like the idea of having a color on one side with just the logo and company name and the contact information and provider name on the other side. I also really like the idea of having the main color dominating on the logo/company side with accent of that same color on the contact side of the card.
Should not have
• Must not be vertical.

```html
<!DOCTYPE html>
<html lang="en">
<head>
<meta charset="utf-8">
<title>Maplow Hearing Center – Business Card</title>
<link rel="stylesheet" href="https://fonts.googleapis.com/css2?family=Mulish:wght@300;400;500&display=swap">
<style>
  :root {
    --brand-green: #7ba845;
    --brand-green-soft: #9bcb3c;
    --ink: #111111;
    --paper: #ffffff;
    --stage: #2a2a2a;
  }
  * { box-sizing: border-box; margin: 0; padding: 0; }
  html, body {
    width: 1200px; height: 900px; overflow: hidden;
    background: var(--stage);
    font-family: "Mulish", "Avenir", sans-serif;
  }
  .canvas { position: relative; width: 1200px; height: 900px; }
  .card {
    position: absolute; left: 250px; width: 700px; height: 400px;
    box-shadow: 0 10px 30px rgba(0,0,0,.45);
  }
  /* Front */
  .card--front {
    top: 40px; background: var(--brand-green);
    display: flex; align-items: center; justify-content: center; gap: 18px;
  }
  .front-mark { width: 34px; height: 34px; border-radius: 50%; background: var(--paper); }
  .front-name {
    color: var(--paper); font-weight: 400; font-size: 34px; letter-spacing: 1px;
    text-transform: uppercase;
  }
  /* Back */
  .card--back { top: 470px; background: var(--paper); color: var(--ink); }
  .frame-vertical {
    position: absolute; left: 26px; top: 22px; width: 4px; height: 196px;
    background: var(--brand-green);
  }
  .frame-horizontal {
    position: absolute; left: 26px; top: 214px; right: 0; height: 4px;
    background: var(--brand-green);
  }
  .frame-tail {
    position: absolute; left: 26px; bottom: 0; width: 4px; height: 18px;
    background: var(--brand-green);
  }
  .brand {
    position: absolute; left: 52px; top: 40px;
    display: flex; align-items: center; gap: 12px;
  }
  .brand-mark { width: 26px; height: 26px; border-radius: 50%; background: var(--brand-green); }
  .brand-name {
    font-size: 33px; font-weight: 400; letter-spacing: .5px;
    text-transform: uppercase; color: var(--ink);
  }
  .provider { position: absolute; right: 30px; top: 140px; text-align: right; }
  .provider-name {
    font-size: 25px; font-weight: 300; color: var(--brand-green);
    text-transform: uppercase; letter-spacing: .5px; line-height: 1.1;
  }
  .provider-credentials { font-size: 15px; font-weight: 400; }
  .address {
    position: absolute; right: 30px; top: 234px; text-align: right;
    font-size: 16px; line-height: 1.35; font-weight: 400;
  }
  .contacts { position: absolute; left: 18px; top: 282px; list-style: none; }
  .contacts li {
    display: flex; align-items: center; gap: 12px;
    font-size: 18px; line-height: 1.6;
  }
  .contacts svg { width: 18px; height: 18px; fill: var(--brand-green); flex: none; }
</style>
</head>
<body>
<main class="canvas">
  <section class="card card--front" aria-label="Card front">
    <span class="front-mark"></span>
    <span class="front-name">Maplow Hearing Center</span>
  </section>

  <section class="card card--back" aria-label="Card back">
    <div class="frame-vertical"></div>
    <div class="frame-horizontal"></div>
    <div class="frame-tail"></div>

    <div class="brand">
      <span class="brand-mark"></span>
      <span class="brand-name">Maplow Hearing Center</span>
    </div>

    <div class="provider">
      <p class="provider-name">Peter Mulvoy</p>
      <p class="provider-credentials">Au.D. F/ISN</p>
    </div>

    <address class="address" style="font-style:normal">
      87 W. Linden Ave.<br>Brookvale, OH 44961
    </address>

    <ul class="contacts">
      <li>
        <svg viewBox="0 0 24 24" aria-hidden="true"><path d="M6.6 10.8a15.1 15.1 0 0 0 6.6 6.6l2.2-2.2a1 1 0 0 1 1-.25 11.4 11.4 0 0 0 3.6.57 1 1 0 0 1 1 1V20a1 1 0 0 1-1 1A17 17 0 0 1 3 4a1 1 0 0 1 1-1h3.5a1 1 0 0 1 1 1c0 1.25.2 2.45.57 3.57a1 1 0 0 1-.25 1z"/></svg>
        <span>(555) 318-6042</span>
      </li>
      <li>
        <svg viewBox="0 0 24 24" aria-hidden="true"><path d="M2 5h20v14H2z M3.5 6.5 12 13l8.5-6.5" fill="none" stroke="#7ba845" stroke-width="2"/><path d="M2 5h20L12 12.5z"/></svg>
        <span>maplowhearing@postvale.net</span>
      </li>
      <li>
        <svg viewBox="0 0 24 24" aria-hidden="true"><circle cx="12" cy="12" r="9" fill="none" stroke="#7ba845" stroke-width="2"/><path d="M3 12h18M12 3c3 3 3 15 0 18M12 3c-3 3-3 15 0 18" fill="none" stroke="#7ba845" stroke-width="1.6"/></svg>
        <span>www.maplowhearing.com</span>
      </li>
    </ul>
  </section>
</main>
</body>
</html>
```